BrightNomadRx.com Blog Design (Travel, Lifestyle, and Life Hacking blog)

I am launching a lifestyle blog about my life. I'm a doctor who travels the world trying the best restaurants, airlines and trying to have as much fun as possible. I also invest in startups, and am always trying new tricks to make life better. I also plan to write about various other topics, but essentially it is about travel, lifestyle and medicine. I need a creative and really awesome looking design for a new wordpress blog called BrightNomadRx

Target Market(s)

Physicians, Entrepreneurs, Travellers

Industry/Entity Type

Airlines

Number of Pages Required

1 page

Font styles to use
Serif

Requirements
Must have
• Slick looking graphics with a highly professional modern feel

```html
<!DOCTYPE html>
<html lang="en">
<head>
<meta charset="utf-8">
<title>BrightNomadRx — the story of my life</title>
<link href="https://fonts.googleapis.com/css2?family=Roboto:ital,wght@0,300;0,400;0,500;0,700;1,300&display=swap" rel="stylesheet">
<style>
  :root {
    --accent: #1d9bb3;
    --ink: #3a3a3a;
    --body: #555;
    --muted: #8a8a8a;
    --rule: #dcdcdc;
    --footer-bg: #cfcfcf;
    --footer-ink: #a9a9a9;
    --white: #fff;
  }
  * { box-sizing: border-box; margin: 0; padding: 0; }
  html, body { width: 1200px; height: 2425px; overflow: hidden; background: var(--white); }
  body { position: relative; font-family: "Roboto", Arial, sans-serif; color: var(--ink); }

  /* top navigation */
  .topbar { position: absolute; left: 0; top: 0; width: 1200px; height: 53px; border-bottom: 1px solid #e6e6e6; }
  .nav { position: absolute; left: 161px; top: 24px; display: flex; list-style: none; }
  .nav li { font-size: 11px; letter-spacing: 2.6px; color: var(--ink); text-transform: uppercase; }
  .nav li:nth-child(1) { width: 71px; }
  .nav li:nth-child(2) { width: 137px; }
  .nav li:nth-child(3) { width: 97px; }
  .search { position: absolute; left: 890px; top: 27px; width: 115px; border-bottom: 1px solid #bbb; font-size: 8px; letter-spacing: 1px; color: var(--muted); padding-bottom: 2px; }
  .search-icon { position: absolute; left: 1011px; top: 26px; }

  /* brand */
  .brand { position: absolute; left: 0; top: 78px; width: 1200px; text-align: center; }
  .brand-name { font-family: "Roboto", Arial, sans-serif; font-weight: 400; font-size: 38px; color: var(--ink); line-height: 1; }
  .brand-tagline { font-weight: 300; font-size: 18px; color: var(--muted); margin-top: 4px; }

  /* hero */
  .hero { position: absolute; left: 0; top: 166px; width: 1200px; height: 292px;
    background: linear-gradient(180deg, #7fb6d6 0%, #5d8a55 30%, #3f6b3a 52%, #2f9cc4 66%, #56b7d8 82%, #b8c46a 100%); }
  .hero-copy { position: absolute; left: 0; top: 246px; width: 1200px; text-align: center; color: var(--white); }
  .hero-kicker { font-weight: 700; font-size: 17px; letter-spacing: .5px; }
  .hero-bar { width: 68px; height: 2px; background: var(--white); margin: 19px auto 20px; }
  .hero-line { font-weight: 400; font-size: 21px; line-height: 23px; }
  .hero-dots { position: absolute; left: 565px; top: 436px; display: flex; gap: 6px; }
  .hero-dots span { width: 11px; height: 11px; border: 1.5px solid var(--white); border-radius: 50%; }
  .hero-dots span.is-active { background: var(--white); }

  /* posts */
  .post { position: absolute; left: 161px; width: 600px; text-align: center; }
  .post-place { font-weight: 700; font-size: 18px; color: var(--ink); line-height: 22px; }
  .underline { width: 38px; height: 3px; background: var(--accent); margin: 5px auto 0; }
  .post-title { font-style: italic; font-weight: 300; font-size: 19px; color: var(--ink); margin-top: 5px; line-height: 24px; }
  .post-date { font-size: 10.5px; color: var(--body); margin-top: 4px; }
  .post-photo { display: block; width: 600px; height: 300px; margin-top: 10px; }
  .post-excerpt { text-align: left; font-size: 10px; line-height: 12.5px; color: var(--body); margin-top: 14px; }
  .read-more { font-size: 10px; color: var(--body); margin-top: 13px; }
  .post-rule { position: absolute; left: 161px; width: 600px; height: 1px; background: var(--rule); }
  .older { position: absolute; left: 161px; top: 2074px; font-weight: 500; font-size: 17px; color: var(--muted); }

  /* sidebar */
  .widget-title { position: absolute; left: 776px; font-weight: 700; font-size: 17px; color: var(--ink); }
  .widget-title::after { content: ""; display: block; width: 38px; height: 3px; background: var(--accent); margin-top: 6px; }
  .side-rule { position: absolute; left: 776px; width: 262px; height: 1px; background: var(--rule); }
  .about-photo { position: absolute; left: 776px; top: 550px; width: 262px; height: 185px;
    background: radial-gradient(ellipse at center, #d9e2e8 0%, #eef1f3 60%, #f7f7f7 100%); }
  .side-text { position: absolute; left: 776px; width: 262px; font-size: 9.6px; line-height: 12px; color: var(--body); }
  .side-more { position: absolute; left: 776px; width: 262px; text-align: center; font-size: 10px; color: var(--body); }
  .social { position: absolute; display: flex; list-style: none; }
  .social li { width: 14px; height: 14px; border-radius: 50%; background: #9a9a9a; }
  .social li.is-accent { background: var(--accent); }

  .recent { position: absolute; left: 776px; top: 1053px; list-style: none; }
  .recent li { position: relative; height: 106px; }
  .recent-thumb { position: absolute; left: 0; top: 0; width: 96px; height: 82px; }
  .recent-title { position: absolute; left: 110px; top: 0; width: 160px; font-style: italic; font-weight: 300; font-size: 17px; line-height: 21px; color: var(--ink); }
  .recent-date { font-style: normal; display: block; font-size: 10px; color: var(--body); margin-top: 5px; }

  .places { position: absolute; left: 776px; top: 1456px; width: 262px; list-style: none; }
  .places li { display: flex; justify-content: space-between; font-size: 12.5px; color: var(--ink); height: 25px; line-height: 20px; border-bottom: 1px solid #c8c8c8; }

  .email { position: absolute; left: 776px; top: 1796px; width: 262px; height: 23px; background: #f1f1f1; font-style: italic; font-size: 9px; color: #aaa; padding: 6px 7px; }
  .subscribe { position: absolute; left: 776px; top: 1826px; font-size: 10px; color: var(--body); }

  .photo-grid { position: absolute; left: 776px; top: 1936px; width: 262px; display: grid; grid-template-columns: 72px 72px 98px; grid-template-rows: 66px 86px 63px; column-gap: 10px; row-gap: 8px; }

  /* footer */
  .footer { position: absolute; left: 0; top: 2212px; width: 1200px; height: 213px; background: var(--footer-bg); text-align: center; }
  .footer .brand-name { color: var(--footer-ink); margin-top: 54px; }
  .footer .brand-tagline { color: var(--footer-ink); }
  .footer .social { left: 503px; top: 135px; gap: 28px; }
  .footer .social li { background: var(--footer-ink); width: 16px; height: 16px; }
</style>
</head>
<body>

<header class="topbar">
  <ul class="nav">
    <li>Home</li>
    <li>Recent Post</li>
    <li>Places</li>
    <li>About</li>
  </ul>
  <div class="search">SEARCH</div>
  <svg class="search-icon" width="14" height="14" viewBox="0 0 14 14" aria-hidden="true">
    <circle cx="5.6" cy="5.6" r="4.3" fill="none" stroke="#222" stroke-width="1.8"/>
    <line x1="8.8" y1="8.8" x2="13" y2="13" stroke="#222" stroke-width="2"/>
  </svg>
</header>

<div class="brand">
  <div class="brand-name">BrightNomadRx</div>
  <div class="brand-tagline">the story of my life</div>
</div>

<section class="hero" role="img" aria-label="Photo of a lakeside temple with tiered roofs and green hills in Bali"></section>
<div class="hero-copy">
  <div class="hero-kicker">WELCOME TO MY SITE</div>
  <div class="hero-bar"></div>
  <div class="hero-line">I'll be in Bali</div>
  <div class="hero-line">on</div>
  <div class="hero-line">[ 7.15.2017 ]</div>
</div>
<div class="hero-dots"><span></span><span class="is-active"></span><span></span><span></span></div>

<main>
  <article class="post" style="top:503px">
    <h2 class="post-place">Grecia</h2>
    <div class="underline"></div>
    <h3 class="post-title">Restaurant Balcony, Santorini</h3>
    <p class="post-date">November 09, 2016</p>
    <div class="post-photo" role="img" aria-label="Photo of a balcony with potted plants overlooking the sea and a blue-domed church in Santorini" style="background:linear-gradient(180deg,#4d8fd6 0%,#7fb0e0 25%,#2e6fa6 45%,#c9a070 70%,#9a5a3c 100%)"></div>
    <p class="post-excerpt">Lorem ipsum dolor sit amet, consectetur adipiscing elit. Proin at sapien rutrum, fermentum risus at, mattis nisi. Duis ullamcorper mauris at vehicula aliquet. Vestibulum ante ipsum primis in faucibus orci luctus et ultrices posuere cubilia Curae; Vivamus scele-risque sapien magna.</p>
    <p class="read-more">| Read More |</p>
  </article>
  <div class="post-rule" style="top:995px"></div>

  <article class="post" style="top:1022px">
    <h2 class="post-place">China</h2>
    <div class="underline"></div>
    <h3 class="post-title">The great wall</h3>
    <p class="post-date">June 05, 2015</p>
    <div class="post-photo" role="img" aria-label="Photo of the Great Wall winding over green hills under a blue sky" style="background:linear-gradient(180deg,#2f79c9 0%,#8fbbe6 28%,#5e8d3e 45%,#3f7a2a 70%,#8a6a55 100%)"></div>
    <p class="post-excerpt">Lorem ipsum dolor sit amet, consectetur adipiscing elit. Proin at sapien rutrum, fermentum risus at, mattis nisi. Duis ullamcorper mauris at vehicula aliquet. Vestibulum ante ipsum primis in faucibus orci luctus et ultrices posuere cubilia Curae; Vivamus scele-risque sapien magna.</p>
    <p class="read-more">| Read More |</p>
  </article>
  <div class="post-rule" style="top:1513px"></div>

  <article class="post" style="top:1543px">
    <h2 class="post-place">Nepal</h2>
    <div class="underline"></div>
    <h3 class="post-title">Himalaya</h3>
    <p class="post-date">July 10, 2014</p>
    <div class="post-photo" role="img" aria-label="Photo of a hiker facing snow-covered Himalayan peaks" style="background:linear-gradient(180deg,#2a6fbf 0%,#6fa2d8 25%,#e8eef4 45%,#8fa6bf 65%,#5a6672 100%)"></div>
    <p class="post-excerpt">Lorem ipsum dolor sit amet, consectetur adipiscing elit. Proin at sapien rutrum, fermentum risus at, mattis nisi. Duis ullamcorper mauris at vehicula aliquet. Vestibulum ante ipsum primis in faucibus orci luctus et ultrices posuere cubilia Curae; Vivamus scele-risque sapien magna.</p>
    <p class="read-more">| Read More |</p>
  </article>

  <div class="older">Older posts</div>
</main>

<aside>
  <h2 class="widget-title" style="top:503px">About me</h2>
  <div class="about-photo" role="img" aria-label="Photo of the blogger in a white coat holding up two large capsules"></div>
  <p class="side-text" style="top:747px">Lorem ipsum dolor sit amet, consectetur adipiscing elit. Proin at sapien rutrum, fermentum risus at, mattis nisi. Duis ullamcorper mauris at vehicula aliquet. Vestibulum ante ipsum primis in faucibus orci luctus et ultrices posuere cubilia Curae; Vivamus scelerisque sapien magna.</p>
  <p class="side-more" style="top:829px">| Read More |</p>
  <div class="side-rule" style="top:860px"></div>

  <h2 class="widget-title" style="top:881px">Follow me</h2>
  <ul class="social" style="left:812px;top:927px;gap:29px" aria-label="Social links">
    <li></li><li class="is-accent"></li><li></li><li></li><li></li>
  </ul>
  <div class="side-rule" style="top:975px"></div>

  <h2 class="widget-title" style="top:996px">Recent Posts</h2>
  <ul class="recent">
    <li>
      <div class="recent-thumb" role="img" aria-label="Thumbnail of the Great Wall" style="background:linear-gradient(180deg,#3b82cc,#6e9a48 55%,#8a6a55)"></div>
      <div class="recent-title">The great wall<span class="recent-date">June 05, 2015</span></div>
    </li>
    <li>
      <div class="recent-thumb" role="img" aria-label="Thumbnail of a Santorini balcony" style="background:linear-gradient(180deg,#5b97d8,#2e6fa6 45%,#b07a55)"></div>
      <div class="recent-title">Restaurant Balcony, Santorini<span class="recent-date">November 09, 2016</span></div>
    </li>
    <li>
      <div class="recent-thumb" role="img" aria-label="Thumbnail of the Great Wall" style="background:linear-gradient(180deg,#3b82cc,#6e9a48 55%,#8a6a55)"></div>
      <div class="recent-title">The great wall<span class="recent-date">June 05, 2015</span></div>
    </li>
  </ul>
  <div class="side-rule" style="top:1376px"></div>

  <h2 class="widget-title" style="top:1408px">Places</h2>
  <ul class="places">
    <li><span>North America</span><span>11</span></li>
    <li><span>South America</span><span>4</span></li>
    <li><span>Africa</span><span>6</span></li>
    <li><span>Europe</span><span>8</span></li>
    <li><span>Middle East</span><span>2</span></li>
    <li><span>Asia</span><span>3</span></li>
    <li><span>Oceania</span><span>1</span></li>
    <li><span>Australia</span><span>5</span></li>
  </ul>
  <div class="side-rule" style="top:1686px"></div>

  <h2 class="widget-title" style="top:1718px">Subscribe To Blog Via Email</h2>
  <p class="side-text" style="top:1760px">Enter your email address to subscribe to this blog and receive notifications of new posts by email.</p>
  <div class="email">Enter your email</div>
  <div class="subscribe">| Subscribe |</div>
  <div class="side-rule" style="top:1862px"></div>

  <h2 class="widget-title" style="top:1896px">My Photos</h2>
  <div class="photo-grid">
    <div role="img" aria-label="Beach with palm leaves" style="background:linear-gradient(180deg,#4fb6d8,#e8d9b0)"></div>
    <div role="img" aria-label="Elephant on a beach" style="background:linear-gradient(180deg,#5aa8d0,#b58a68)"></div>
    <div role="img" aria-label="Jet ski on turquoise water" style="background:linear-gradient(180deg,#2aa3c0,#7fd0e0)"></div>
    <div role="img" aria-label="Parachute jump over the sea" style="background:linear-gradient(180deg,#3f8fd0,#e0a040)"></div>
    <div role="img" aria-label="Snowboarder on a slope" style="background:linear-gradient(180deg,#2d6fb0,#dfe8f0)"></div>
    <div role="img" aria-label="Snowy mountain view" style="background:linear-gradient(180deg,#6fa6d8,#e8eef3)"></div>
    <div role="img" aria-label="Pelican close-up" style="background:linear-gradient(180deg,#7a8a90,#d8d2c6)"></div>
    <div role="img" aria-label="Colourful woven textiles" style="background:linear-gradient(135deg,#c8302a,#e8a0a0)"></div>
    <div role="img" aria-label="Diver underwater" style="background:linear-gradient(180deg,#1f5cb8,#3a8ad8)"></div>
  </div>
</aside>

<footer class="footer">
  <div class="brand-name">BrightNomadRx</div>
  <div class="brand-tagline">the story of my life</div>
  <ul class="social" aria-label="Social links">
    <li></li><li></li><li></li><li></li><li></li>
  </ul>
</footer>

</body>
</html>
```